Web Design Project - Old Brackley (Bar)

We need a website for a new wine bar/hotel opening in Sydney's Kings Cross area. The concept is a rustic Australiana bar. We intend to use raw materials (sandstone, rusty metal etc) and lots of greenery/plants. It is set to be stylish and accessible to a young and middle age clientele.

The idea is to bring the outside inside.

The venue can cater for 450 people and is in one of the major nightclub strips in Australia. The demographic differs from celebrities to backpackers.

Target Market(s)

We are targeting 23yr - 40yr olds.

Industry/Entity Type

Hotel

Requirements
Must have
• What I want is a design to reflect is the fit out of the bar. We would like to see a rustic design to reflect the theme of the bar. The theme behind the fit out will be "bringing the outside inside" with lots of plants, wet walls etc.. There will be exposed brickwork, sandstone, timber and rusted steel with laser cut designs throughout the venue.
Nice to have
• I've attached some 3D designs that the venue will be roughly based on.

```html
<!DOCTYPE html>
<html lang="en">
<head>
<meta charset="utf-8">
<title>Old Brackley</title>
<link rel="stylesheet" href="https://fonts.googleapis.com/css2?family=Federo&family=Arimo:wght@400;700&display=swap">
<style>
:root{
  --page:#ffffff;
  --bar:#151312;
  --panel:#1b1817;
  --panel-edge:#2a2523;
  --footer:#050505;
  --text:#ffffff;
  --muted:#a8a4a0;
  --accent:#e3dc3c;
  --bullet:#c8c21e;
  --frame:#bdbdbd;
  --hero-frame:#3e3a37;
  --body-text:#e8e4e0;
}
*{margin:0;padding:0;box-sizing:border-box}
html,body{width:1200px;height:900px;overflow:hidden;background:var(--page)}
body{position:relative;font-family:"Arimo",Arial,sans-serif;color:var(--text)}
.site{position:absolute;left:87px;top:0;width:1028px;height:900px}
.venue-backdrop{position:absolute;left:0;top:40px;width:1028px;height:777px;
  background:linear-gradient(90deg,#6d5a4a 0%,#9a8a78 6%,#5a4a3e 12%,#3a2e26 14%,#2d2420 86%,#6a3a22 92%,#8a5a3e 100%)}
.venue-floor{position:absolute;left:0;top:560px;width:1028px;height:257px;
  background:linear-gradient(180deg,rgba(120,80,60,0),rgba(150,110,90,.55))}
.top-bar{position:absolute;left:0;top:0;width:1028px;height:40px;background:var(--bar);border-bottom:1px solid #2c2826}
.top-nav a{position:absolute;top:13px;font-size:12px;color:var(--muted);text-decoration:none}
.top-nav a.current{color:var(--text)}
.top-nav .marker{position:absolute;left:157px;top:28px}
.search-field{position:absolute;left:646px;top:11px;width:169px;height:18px;background:#2a2624;border:1px solid #55504c}
.search-button{position:absolute;left:821px;top:11px;width:62px;height:18px;background:#3a3634;border:1px solid #66615d;color:#cfcac6;font-size:11px;text-align:center;line-height:16px}
.panel{position:absolute;left:134px;top:40px;width:760px;height:777px;background:linear-gradient(180deg,var(--panel),#141110);border-left:1px solid var(--panel-edge);border-right:1px solid var(--panel-edge)}
.brand{position:absolute;left:13px;top:10px;width:118px;height:70px;display:flex;align-items:center;justify-content:center;gap:6px;font-size:12px;color:#e8dcc4;letter-spacing:.5px}
.brand .mark{width:10px;height:10px;background:#b59b72}
.social{position:absolute;top:14px;width:28px;height:28px;border-radius:50%}
.social.one{left:681px;background:#3b5a9a}
.social.two{left:718px;background:#3aa8e0}
.hero{position:absolute;left:13px;top:90px;width:735px;height:207px;border:2px solid var(--hero-frame);
  background:linear-gradient(90deg,#3a2a14,#8a6a2a 25%,#c89a3a 40%,#4a3a22 55%,#2a2a12 70%,#6a5a3a 85%,#3a2e20)}
h2{font-family:"Federo",sans-serif;font-weight:400;font-size:19px;position:absolute;white-space:nowrap}
.feature h2{top:316px}
.feature .photo{position:absolute;top:361px;width:212px;height:123px;border:2px solid var(--frame)}
.feature p{position:absolute;top:509px;width:255px;font-size:10.5px;line-height:16px;text-align:justify;color:var(--body-text)}
.read-more{position:absolute;top:589px;font-size:8px;font-weight:700;color:var(--text);text-decoration:none}
.menu-list{list-style:none;position:absolute;left:605px;top:357px}
.menu-list li{position:relative;height:25px;padding-left:24px;font-size:10.5px;color:var(--body-text)}
.menu-list li::before{content:"";position:absolute;left:0;top:3px;border-left:6px solid var(--bullet);border-top:4px solid transparent;border-bottom:4px solid transparent}
.about h2,.contact h2{top:641px;color:var(--accent)}
.about p{position:absolute;left:16px;top:673px;width:562px;font-size:10.5px;line-height:16px;text-align:justify;color:var(--body-text);hyphens:auto;-webkit-hyphens:auto}
.contact h2{color:var(--text);left:613px}
.contact address{position:absolute;left:633px;top:672px;font-style:normal;font-size:9px;font-weight:700;line-height:19.5px}
.footer{position:absolute;left:0;top:817px;width:1028px;height:83px;background:var(--footer);border-top:1px solid #3a3634}
.footer-nav a{position:absolute;top:18px;font-size:12px;color:var(--text);text-decoration:none}
.copyright{position:absolute;top:52px;width:100%;text-align:center;font-size:8px;font-weight:700}
</style>
</head>
<body>
<div class="site">
  <div class="venue-backdrop" role="img" aria-label="Interior of the bar with sandstone walls, timber ceiling, plants and patterned tile floor"></div>
  <div class="venue-floor"></div>

  <header class="top-bar">
    <nav class="top-nav">
      <a class="current" href="#" style="left:146px">Home</a>
      <a href="#" style="left:206px">About Us</a>
      <a href="#" style="left:281px">Menu</a>
      <a href="#" style="left:338px">Events</a>
      <a href="#" style="left:402px">Contact Us</a>
      <svg class="marker" width="8" height="6" viewBox="0 0 8 6"><path d="M0 6 L4 0 L8 6Z" fill="#b8b090"/></svg>
    </nav>
    <div class="search-field"></div>
    <div class="search-button">Search</div>
  </header>

  <main class="panel">
    <div class="brand"><span class="mark"></span>OLD BRACKLEY</div>
    <span class="social one"></span>
    <span class="social two"></span>

    <div class="hero" role="img" aria-label="Wine barrel with glasses of white and red wine and wine bottles"></div>

    <section class="feature">
      <h2 style="left:15px">Lorem Ipsum</h2>
      <div class="photo" style="left:36px;background:linear-gradient(135deg,#4a2a1a,#7a5a2a 45%,#c8b060 70%,#5a3a20)" role="img" aria-label="Wine bottles, grapes and cheese on a table"></div>
      <p style="left:16px">Lorem Ipsum is simply dummy text of the printing and typesetting industry. Lorem Ipsum has been the industry's standard dummy text ever since the 1500s, when an unknown printer took a galley</p>
      <a class="read-more" href="#" style="left:213px">Read More...</a>
    </section>

    <section class="feature">
      <h2 style="left:297px">Lorem Ipsum is simply</h2>
      <div class="photo" style="left:318px;background:linear-gradient(135deg,#c8a040,#8a2020 40%,#2a1a14 65%,#d0a040)" role="img" aria-label="Wine bottles lying in a rack"></div>
      <p style="left:299px">Lorem Ipsum is simply dummy text of the printing and typesetting industry. Lorem Ipsum has been the industry's standard dummy text ever since the 1500s, when an unknown printer took a galley</p>
      <a class="read-more" href="#" style="left:496px">Read More...</a>
    </section>

    <section class="menu">
      <h2 style="left:584px;top:316px">Our Menu</h2>
      <ul class="menu-list">
        <li>Appetizer</li><li>Soups</li><li>Salads</li><li>Main Course (Curries)</li>
        <li>Tandoori Specials</li><li>Freshly Baked Breads</li><li>Australian Specials</li>
        <li>Desserts</li><li>Main Course (Curries)</li>
      </ul>
      <a class="read-more" href="#" style="left:707px">More...</a>
    </section>

    <section class="about">
      <h2 style="left:16px">About OLD BRACKLEY</h2>
      <p>Lorem Ipsum is simply dummy text of the printing and typesetting industry. Lorem Ipsum has been the industry's stan&shy;dard dummy text ever since the 1500s, when an unknown printer took a galley of type and scrambled it to make a type specimen book. It has survived not only five centuries, but also the leap into electronic typesetting, remaining essen&shy;tially unchanged. It was popularised in the 1960s with the release of Lettrafoil sheets containing Lorem Ipsum pas&shy;sages, and more recently with desktop publishing software like Quillset Layout including versions of Lorem Ipsum.</p>
    </section>

    <section class="contact">
      <h2>Contact :</h2>
      <address>OLD BRACKLEY<br>#&nbsp; 412 Ridgeway Lane<br>Lorem Ipsum is simply<br>Kestrel Bay 3150, Wendmoor.</address>
    </section>
  </main>

  <footer class="footer">
    <nav class="footer-nav">
      <a href="#" style="left:347px">Home</a>
      <a href="#" style="left:409px">About Us</a>
      <a href="#" style="left:486px">Menu</a>
      <a href="#" style="left:546px">Events</a>
      <a href="#" style="left:612px">Contact Us</a>
    </nav>
    <p class="copyright">© 2013 OLD BRACKLEY All Rights Reserved.</p>
  </footer>
</div>
</body>
</html>
```